Building company buisness cards

We are looking for a sharp modern new look for our business cards.We are a New Zealand based company that specialises in house and land packages.We have attached a photo of the current logo and would like to see if it can be improved somehow if needed.We are open to any colours but we have chosen Black and White at this stage. Feel free to change the font and make the logo smarter looking.Play with the colours and see what looks best.We want a card that looks so good know one will want to throw it away!

Target Market(s)

Building profesonals, home buyers

Industry/Entity Type

Building

Contact Information for Business Card

Derek Haskins
0274930268
derekh@stonerange.co.nz

Font styles to use
Serif
Sans Serif

Colors

Designer to choose colors to be used in the design.

Requirements
Must have
• Just the logo on one side and details on the other
• Clean simple looking card
Nice to have
• Round corners and detail like raised or spot UV
• Something that stands out
Should not have
• To title needed, Director etc

```html
<!DOCTYPE html>
<html lang="en">
<head>
<meta charset="utf-8">
<title>Stonerange Business Card</title>
<link href="https://fonts.googleapis.com/css2?family=Oswald:wght@500&family=Work+Sans:wght@400;600&display=swap" rel="stylesheet">
<style>
  :root {
    --backdrop: #161616;
    --card: #1d1d1d;
    --card-edge: #262626;
    --ink: #ffffff;
  }
  * { margin: 0; padding: 0; box-sizing: border-box; }
  html, body {
    width: 1200px;
    height: 900px;
    overflow: hidden;
    background: var(--backdrop);
  }
  .sheet {
    width: 1200px;
    height: 900px;
    display: flex;
    flex-direction: column;
    align-items: center;
    justify-content: center;
    gap: 36px;
  }
  .card {
    position: relative;
    width: 630px;
    height: 360px;
    background: linear-gradient(135deg, var(--card) 0%, var(--card-edge) 100%);
    border-radius: 10px;
    color: var(--ink);
  }
  /* front */
  .card--front {
    display: flex;
    align-items: center;
    justify-content: center;
  }
  .brand__name {
    font-family: "Work Sans", sans-serif;
    font-weight: 600;
    font-size: 58px;
    letter-spacing: -0.5px;
    color: var(--ink);
  }
  /* back */
  .card--back { font-family: "Work Sans", sans-serif; }
  .identity {
    position: absolute;
    left: 70px;
    top: 138px;
    width: 230px;
    text-align: right;
  }
  .identity__name {
    font-family: "Oswald", sans-serif;
    font-weight: 500;
    font-size: 30px;
    letter-spacing: 1px;
    line-height: 36px;
    text-transform: uppercase;
    white-space: nowrap;
  }
  .divider {
    position: absolute;
    left: 322px;
    top: 124px;
    width: 2px;
    height: 64px;
    background: var(--ink);
  }
  .contacts {
    position: absolute;
    left: 344px;
    top: 122px;
    list-style: none;
    font-size: 16px;
    letter-spacing: 0.4px;
    line-height: 23px;
  }
  .contacts li { display: flex; align-items: center; gap: 10px; white-space: nowrap; }
  .contacts svg { width: 11px; height: 11px; flex: none; }
  .address {
    position: absolute;
    left: 118px;
    bottom: 52px;
    font-size: 16px;
    letter-spacing: 0.5px;
  }
</style>
</head>
<body>
<main class="sheet">
  <section class="card card--front" aria-label="Card front">
    <span class="brand__name">Stonerange</span>
  </section>

  <section class="card card--back" aria-label="Card back">
    <div class="identity">
      <p class="identity__name">Derek Haskins</p>
    </div>
    <div class="divider"></div>
    <ul class="contacts">
      <li>
        <svg viewBox="0 0 12 12" aria-hidden="true"><path d="M2.5 1h2l1 2.5-1.3 1a6 6 0 0 0 3.3 3.3l1-1.3L11 7.5v2a1 1 0 0 1-1 1A9 9 0 0 1 1.5 2a1 1 0 0 1 1-1z" fill="var(--ink)"/></svg>
        0274930268
      </li>
      <li>
        <svg viewBox="0 0 12 12" aria-hidden="true"><rect x="1" y="2.5" width="10" height="7" fill="none" stroke="var(--ink)" stroke-width="1.2"/><path d="M1 2.5l5 4 5-4" fill="none" stroke="var(--ink)" stroke-width="1.2"/></svg>
        derekh@stonerange.co.nz
      </li>
      <li>
        <svg viewBox="0 0 12 12" aria-hidden="true"><circle cx="6" cy="6" r="5" fill="none" stroke="var(--ink)" stroke-width="1"/><ellipse cx="6" cy="6" rx="2.2" ry="5" fill="none" stroke="var(--ink)" stroke-width="1"/><path d="M1 6h10" stroke="var(--ink)" stroke-width="1"/></svg>
        www.stonerange.co.nz
      </li>
    </ul>
    <p class="address">142b Halsey Road, Christchurch, NZ, 8023</p>
  </section>
</main>
</body>
</html>
```